Vanta Forge - Business Cards

We are a consultancy to help builders to optimize their planning in order to save building costs. For that reason we need a clean and professional business card for our high-priced services. A QR code should lead to the contact information needed.

```html
<!DOCTYPE html>
<html lang="en">
<head>
<meta charset="utf-8">
<title>Vanta Forge – Business Cards</title>
<link href="https://fonts.googleapis.com/css2?family=Roboto:wght@400;500;700&display=swap" rel="stylesheet">
<style>
  :root {
    --page-bg: #2a2a2a;
    --card-dark: #1f1f20;
    --card-edge: #3a3a3e;
    --gold: #c9a04a;
    --gold-light: #e0bb5e;
    --gold-deep: #a8772e;
    --ink-dark: #2b2b30;
    --text-light: #e8e8e8;
    --text-muted: #9a9a9a;
    --emboss-dark: #1b1b1c;
    --emboss-mid: #2c2c2e;
    --emboss-light: #4a4a4c;
  }
  * { margin: 0; padding: 0; box-sizing: border-box; }
  html, body { width: 1200px; height: 1138px; overflow: hidden; }
  body {
    background: var(--page-bg);
    font-family: "Roboto", Arial, sans-serif;
    position: relative;
  }
  .card {
    position: absolute;
    width: 624px;
    height: 376px;
    border-radius: 16px;
    background: var(--card-dark);
    overflow: hidden;
  }
  .card--front { left: 274px; top: 186px; }
  .card--back { left: 276px; top: 608px; width: 618px; height: 374px; }

  .brand-name {
    position: absolute;
    font-weight: 700;
    letter-spacing: 0.5px;
    white-space: nowrap;
  }
  .card--front .brand-name {
    left: 35px;
    top: 116px;
    font-size: 32px;
    color: var(--gold);
  }
  .front-url {
    position: absolute;
    left: 36px;
    top: 327px;
    font-size: 17px;
    color: var(--text-muted);
  }
  .front-mark-area {
    position: absolute;
    left: 316px;
    top: 22px;
    right: 0;
    bottom: 0;
    border-top-left-radius: 12px;
    background:
      radial-gradient(ellipse at 85% 75%, var(--emboss-light) 0%, transparent 60%),
      linear-gradient(135deg, var(--emboss-dark) 0%, var(--emboss-mid) 55%, #3a3a3c 100%);
    opacity: 0.9;
  }

  .back-art { position: absolute; inset: 0; }
  .contact {
    position: absolute;
    left: 31px;
    top: 88px;
    color: var(--text-light);
  }
  .contact-name {
    font-size: 22px;
    font-weight: 700;
    color: var(--gold-light);
    line-height: 1.1;
  }
  .contact-role {
    font-size: 16px;
    margin-top: 4px;
  }
  .contact-list {
    list-style: none;
    margin-top: 26px;
    font-size: 16.5px;
  }
  .contact-list li {
    display: flex;
    align-items: center;
    height: 24px;
  }
  .contact-list svg {
    width: 14px; height: 14px;
    margin-right: 17px;
    fill: var(--gold);
  }
  .contact-address {
    margin-top: 8px;
    font-size: 16.5px;
    line-height: 24px;
  }
  .card--back .brand-name {
    left: 456px;
    top: 200px;
    transform: translateX(-50%);
    font-size: 28px;
    color: var(--ink-dark);
  }
</style>
</head>
<body>
  <section class="card card--front">
    <div class="front-mark-area" role="img" aria-label="Large embossed brand mark area"></div>
    <div class="brand-name">Vanta Forge</div>
    <div class="front-url">www.vantaforge.com</div>
  </section>

  <section class="card card--back">
    <svg class="back-art" viewBox="0 0 618 374" width="618" height="374" preserveAspectRatio="none" aria-hidden="true">
      <defs>
        <linearGradient id="goldFill" x1="0" y1="0" x2="0" y2="1">
          <stop offset="0" stop-color="#a8772e"/>
          <stop offset="0.45" stop-color="#e0bd62"/>
          <stop offset="0.6" stop-color="#d8b052"/>
          <stop offset="1" stop-color="#a8772e"/>
        </linearGradient>
      </defs>
      <path d="M340 0 C284 50 264 130 268 190 C272 260 294 320 336 374 L618 374 L618 0 Z" fill="#3a3a3e"/>
      <path d="M356 0 C300 50 280 130 284 190 C288 260 310 320 352 374 L618 374 L618 0 Z" fill="url(#goldFill)"/>
    </svg>

    <div class="contact">
      <div class="contact-name">Vanta Forge</div>
      <div class="contact-role">Managing Director</div>
      <ul class="contact-list">
        <li><svg viewBox="0 0 16 16"><path d="M3 2h3l1.5 3.5-2 1.2a8 8 0 0 0 3.8 3.8l1.2-2L14 10v3a1 1 0 0 1-1 1A11 11 0 0 1 2 3a1 1 0 0 1 1-1z"/></svg>828-555-0147</li>
        <li><svg viewBox="0 0 16 16"><path d="M1 3h14v10H1z M2 4l6 5 6-5" fill="none" stroke="#c9a04a" stroke-width="1.5"/></svg>hello@vantaforge.com</li>
        <li><svg viewBox="0 0 16 16"><circle cx="8" cy="8" r="6.5" fill="none" stroke="#c9a04a" stroke-width="1.4"/><path d="M1.5 8h13M8 1.5c-3 3.5-3 9.5 0 13M8 1.5c3 3.5 3 9.5 0 13" fill="none" stroke="#c9a04a" stroke-width="1.2"/></svg>www.vantaforge.com</li>
      </ul>
      <div class="contact-address">18 Larkspur Rd., Millbrook,<br>Eastvale, US 204871</div>
    </div>

    <div class="brand-name">Vanta Forge</div>
  </section>
</body>
</html>
```